Redesign of Grantlyhub.com

We need a redesign of some key-pages on our crowdfunding website for mobile apps, GrantlyHub.com.

- Redesign of homepage
http://www.grantlyhub.com/en

- Redesign of project submission page
http://www.grantlyhub.com/en/submit-your-app/submit-your-app

- Redesign of browsing section
http://www.grantlyhub.com/en/fund-apps

- Redesign of project funding page
http://www.grantlyhub.com/en/fund-apps/sponsor/sketch-riddler?amount=5.00

Design should be highly focused on a great user experience for users of the platform, being in principal mobile developers. So we need a great user experience for mobile developers using our service.

Benchmark designs we particularly like are:
http://www.pledgorama.com/
http://www.tradebitly.com/landing/
http://www.vomba.com/

Design should have a more 'fun, happy to get involved' factor as it has nox.
Updates

Logo's have been uploaded

Target Market(s)

mobile app developers

Industry/Entity Type

Crowdfunding

Requirements
Must have
• Submission forms must have explanation fields next to the form

Homepage should have design in whihc a introductary video can be integrated

```html
<!DOCTYPE html>
<html lang="en">
<head>
<meta charset="utf-8">
<title>GrantlyHub – Support new mobile apps</title>
<link rel="stylesheet" href="https://fonts.googleapis.com/css2?family=Ubuntu:wght@400;500;700&family=Open+Sans:wght@400;600;700&display=swap">
<style>
  :root {
    --page-bg: #0b355c;
    --header-bg: #0d3f6b;
    --navy: #14304e;
    --bar-navy: #24466e;
    --lime: #8dc21f;
    --link-lime: #b5e31c;
    --hero-bg: #1f2430;
    --builder-blue: #3b8ad9;
    --press-gray: #8a8a8a;
    --white: #ffffff;
  }
  * { box-sizing: border-box; margin: 0; padding: 0; }
  html, body { width: 1200px; height: 800px; overflow: hidden; }
  body {
    position: relative;
    background: var(--page-bg);
    font-family: "Open Sans", Arial, sans-serif;
  }
  .site-header {
    position: absolute; left: 0; top: 0; width: 1200px; height: 117px;
    background: linear-gradient(180deg, #0a3a64 0%, var(--header-bg) 60%, #0f4676 100%);
  }
  .brand {
    position: absolute; left: 120px; top: 30px;
    display: flex; align-items: center; gap: 12px;
    font-family: "Ubuntu", sans-serif; font-weight: 500;
    font-size: 28px; color: var(--white); text-decoration: none;
  }
  .brand-mark { width: 36px; height: 36px; background: var(--white); border-radius: 4px; }
  .top-links {
    position: absolute; right: 121px; top: 3px;
    font-size: 12.5px; color: var(--white); letter-spacing: .3px;
  }
  .top-links a { color: var(--link-lime); text-decoration: none; }
  .top-links span { margin: 0 6px; }
  .social { position: absolute; left: 968px; top: 92px; display: flex; gap: 5px; }
  .social i { width: 18px; height: 18px; background: #5b8fc4; display: block; border-radius: 2px; }
  .main-nav {
    position: absolute; left: 0; top: 117px; width: 1200px; height: 34px;
    background: linear-gradient(180deg, #fdfdfd 0%, #e6e6e6 55%, #c9c9c9 100%);
    box-shadow: 0 2px 4px rgba(0,0,0,.4);
  }
  .main-nav ul { list-style: none; position: absolute; left: 146px; top: 7px; display: flex; gap: 22px; }
  .main-nav a {
    font-family: "Ubuntu", sans-serif; font-weight: 700; font-size: 14px;
    color: var(--navy); text-decoration: none;
  }
  .main-nav a.current { color: var(--lime); }
  .search {
    position: absolute; left: 846px; top: 6px; width: 234px; height: 21px;
    background: #2b3038; border: 1px solid #111; color: var(--lime);
    font-size: 12px; padding: 2px 9px;
  }
  .search svg { position: absolute; right: 6px; top: 3px; }
  .content {
    position: absolute; left: 120px; top: 151px; width: 960px; height: 649px;
    background: var(--white);
  }
  .hero {
    position: absolute; left: 25px; top: 15px; width: 910px; height: 329px;
    background: var(--hero-bg);
    box-shadow: 0 8px 10px -6px rgba(0,0,0,.5);
  }
  .video-frame {
    position: absolute; left: 12px; top: 10px; width: 576px; height: 305px;
    border: 1px solid var(--white);
    background: radial-gradient(circle at 50% 45%, #2a2f3c 0%, #1f2430 70%);
    color: var(--white); text-align: center;
  }
  .video-art {
    width: 114px; height: 86px; margin: 87px auto 0;
    background: #3a4050; border-radius: 2px;
  }
  .video-frame p { font-family: "Ubuntu", sans-serif; font-size: 19px; margin-top: 14px; }
  .pitch { position: absolute; left: 614px; top: 15px; color: var(--white); font-family: "Ubuntu", sans-serif; }
  .pitch h1 { font-size: 20px; font-weight: 400; letter-spacing: .1px; }
  .pitch h1 b { font-weight: 700; }
  .pitch h2 { font-size: 15px; font-weight: 400; }
  .pitch .builders { color: var(--builder-blue); margin-top: 18px; }
  .pitch .funders { color: var(--lime); margin-top: 12px; }
  .pitch ul { list-style: none; margin: 4px 0 0 47px; font-size: 15px; line-height: 19.5px; }
  .pitch li::before {
    content: "+"; display: inline-block; width: 12px; height: 12px; border-radius: 50%;
    font-size: 11px; line-height: 11px; text-align: center; margin-right: 7px; vertical-align: 1px;
  }
  .builders + ul li::before { background: #2d5f93; color: #a9cff5; }
  .funders + ul li::before { background: #4f7e2a; color: #c6eea0; }
  .btn {
    display: block; height: 35px; width: 171px; border-radius: 3px;
    font-size: 17px; font-weight: 500; color: var(--white); text-align: center; line-height: 34px;
    text-decoration: none;
  }
  .btn-project { background: linear-gradient(#3f86df, #1c56ad); border: 1px solid #6aa5ee; margin: 11px 0 0 52px; }
  .btn-funding { background: linear-gradient(#5fcc32, #2c9414); border: 1px solid #7fe057; margin: 8px 0 0 49px; }
  .featured { position: absolute; left: 27px; top: 365px; font-size: 11.5px; color: #444; letter-spacing: .5px; }
  .press { position: absolute; top: 384px; left: 0; width: 960px; height: 26px; }
  .press span {
    position: absolute; transform: translateX(-50%); white-space: nowrap;
    font-family: "Open Sans", sans-serif; font-weight: 600; font-size: 18px; color: var(--press-gray);
  }
  .section-bar {
    position: absolute; height: 24px; background: var(--bar-navy);
    color: var(--white); font-family: "Ubuntu", sans-serif; font-size: 14.5px; padding: 3px 15px;
  }
  .section-bar em { font-style: normal; color: var(--lime); }
  .section-bar .see-all { position: absolute; right: 28px; top: 3px; color: var(--lime); font-size: 13.5px; text-decoration: none; }
  .app-tiles { position: absolute; left: 40px; top: 474px; display: flex; gap: 20px; }
  .app-tile { width: 96px; text-align: center; }
  .app-tile .icon { width: 96px; height: 95px; border-radius: 9px; box-shadow: 2px 3px 5px rgba(0,0,0,.45); }
  .app-tile p { font-size: 11.5px; color: var(--navy); margin-top: 9px; letter-spacing: .3px; }
  .funder-grid { position: absolute; left: 641px; top: 476px; display: grid; grid-template-columns: repeat(3, 77px); column-gap: 24px; row-gap: 8px; }
  .funder { text-align: center; }
  .funder .avatar { width: 77px; height: 77px; border: 3px solid #3b5b82; border-radius: 6px; }
  .funder p { font-size: 11.5px; font-weight: 700; color: #333; margin-top: 3px; }
</style>
</head>
<body>
  <header class="site-header">
    <a class="brand" href="#"><span class="brand-mark"></span>GrantlyHub</a>
    <nav class="top-links">
      <a href="#">Blog</a><span>|</span><a href="#">Get AAA Certified</a><span>|</span><a href="#">About us</a><span>|</span><a href="#">Login in</a>
    </nav>
    <div class="social" aria-label="Social links"><i></i><i></i><i></i><i></i><i></i></div>
  </header>

  <nav class="main-nav">
    <ul>
      <li><a class="current" href="#">HOME</a></li>
      <li><a href="#">FUND&nbsp; APPS</a></li>
      <li><a href="#">SUBMIT YOUR APP</a></li>
      <li><a href="#">FIND A DEVELOPER</a></li>
      <li><a href="#">HOW IT WORKS</a></li>
      <li><a href="#">REGISTER</a></li>
    </ul>
    <div class="search">Search
      <svg width="14" height="14" viewBox="0 0 14 14"><circle cx="5.5" cy="5.5" r="4" fill="none" stroke="#8dc21f" stroke-width="2"/><line x1="8.5" y1="8.5" x2="13" y2="13" stroke="#8dc21f" stroke-width="2.4"/></svg>
    </div>
  </nav>

  <main class="content">
    <section class="hero">
      <div class="video-frame">
        <div class="video-art" role="img" aria-label="Video player mascot illustration"></div>
        <p>Play Introductory Video</p>
      </div>
      <div class="pitch">
        <h1>SUPPORT <b>NEW MOBILE APPS</b></h1>
        <h2 class="builders">APP BUILDERS:</h2>
        <ul><li>Fund your development</li><li>Build up customers</li><li>Keep 100% ownership</li></ul>
        <a class="btn btn-project" href="#">Start project</a>
        <h2 class="funders">FUNDERS:</h2>
        <ul><li>Up to 120% in return</li><li>Fund per milestone</li><li>Get appstore sales updates</li></ul>
        <a class="btn btn-funding" href="#">Start funding</a>
      </div>
    </section>

    <p class="featured">Featured on:</p>
    <div class="press">
      <span style="left:145px">The Harbor Ledger</span>
      <span style="left:300px">ByteWire</span>
      <span style="left:455px">Datadesk</span>
      <span style="left:642px">StartList</span>
      <span style="left:817px">LaunchPulse</span>
    </div>

    <div class="section-bar" style="left:26px;top:431px;width:594px">Most funded apps:<a class="see-all" href="#">see all &gt;&gt;</a></div>
    <div class="section-bar" style="left:627px;top:431px;width:305px">Most Active <em>Funders:</em></div>

    <div class="app-tiles">
      <div class="app-tile"><div class="icon" role="img" aria-label="Puzzle game app icon" style="background:linear-gradient(#2f7a34,#9a3a2a)"></div><p>TileTinker</p></div>
      <div class="app-tile"><div class="icon" role="img" aria-label="Cartoon mascot app icon" style="background:linear-gradient(#c0161b,#8e0f12)"></div><p>TileTinker</p></div>
      <div class="app-tile"><div class="icon" role="img" aria-label="Letter tile app icon" style="background:linear-gradient(#6a6a6a,#3e3e3e)"></div><p>TileTinker</p></div>
      <div class="app-tile"><div class="icon" role="img" aria-label="Chalkboard word game app icon" style="background:linear-gradient(#2d2d2d 70%,#c27a3a)"></div><p>TileTinker</p></div>
      <div class="app-tile"><div class="icon" role="img" aria-label="Street scene game app icon" style="background:linear-gradient(#8fd2f0,#d9a070)"></div><p>TileTinker</p></div>
    </div>

    <div class="funder-grid">
      <div class="funder"><div class="avatar" role="img" aria-label="Funder profile picture" style="background:#2f4fa8"></div><p>Tov</p></div>
      <div class="funder"><div class="avatar" role="img" aria-label="Funder profile photo" style="background:linear-gradient(#8a6a50,#3c3c50)"></div><p>Milo R...</p></div>
      <div class="funder"><div class="avatar" role="img" aria-label="Funder profile photo" style="background:linear-gradient(#e0e0e0,#555)"></div><p>Henri ...</p></div>
      <div class="funder"><div class="avatar" role="img" aria-label="Funder profile photo" style="background:linear-gradient(#6d8a5a,#4a5a3a)"></div></div>
      <div class="funder"><div class="avatar" role="img" aria-label="Default profile placeholder" style="background:#c6d3e6"></div></div>
      <div class="funder"><div class="avatar" role="img" aria-label="Funder company avatar" style="background:linear-gradient(#3a3a3a,#1a1a1a)"></div></div>
    </div>

    <div class="section-bar" style="left:26px;top:615px;width:594px">Our staff's picks:<a class="see-all" href="#">see all &gt;&gt;</a></div>
  </main>
</body>
</html>
```